Letterhead for invoices and engagement letter

Want to use logos sourced on pixelbazaar to create letterhead templates for word or pdf files

Industry/Entity Type

Legal- law firm

Colors
0054AA
0677BA
7BADD7
CADEEF
E8F1F8

```html
<!DOCTYPE html>
<html lang="en">
<head>
<meta charset="utf-8">
<title>Halden Law PLC – Invoice and Letterhead</title>
<link href="https://fonts.googleapis.com/css2?family=EB+Garamond:ital,wght@0,400;0,500&family=Roboto:ital,wght@0,300;0,400;0,500;1,300&display=swap" rel="stylesheet">
<style>
  :root {
    --backdrop: #c6c5c6;
    --paper: #ffffff;
    --navy: #16253a;
    --ink: #2b3a4e;
    --ink-soft: #4a5566;
    --silver: #c9cbd0;
    --row-shade: #c9c7c9;
    --watermark: #f3f3f4;
  }
  * { margin: 0; padding: 0; box-sizing: border-box; }
  html, body { width: 1200px; height: 1200px; overflow: hidden; }
  body {
    background: var(--backdrop);
    font-family: "Roboto", sans-serif;
    color: var(--ink);
    position: relative;
  }
  .sheet {
    position: absolute;
    width: 519px;
    height: 671px;
    background: var(--paper);
    overflow: hidden;
  }
  .sheet--invoice { left: 62px; top: 268px; }
  .sheet--letter { left: 614px; top: 270px; }
  .abs { position: absolute; }

  /* brand block */
  .brand {
    position: absolute;
    left: 26px; top: 0;
    width: 114px; height: 142px;
    background: var(--navy);
  }
  .brand__disc {
    position: absolute;
    left: 27px; top: 26px;
    width: 60px; height: 60px;
    border-radius: 50%;
    background: var(--silver);
  }
  .brand__name {
    position: absolute;
    left: 0; right: 0; top: 94px;
    text-align: center;
    font-family: "EB Garamond", serif;
    font-weight: 400;
    font-size: 15px;
    line-height: 16px;
    letter-spacing: 0.5px;
    color: var(--silver);
    text-transform: uppercase;
  }

  /* contact list */
  .contacts { position: absolute; list-style: none; }
  .contacts li { display: flex; align-items: center; white-space: nowrap; }
  .contacts svg { flex: none; }
  .contacts--invoice { left: 26px; top: 152px; font-size: 8px; }
  .contacts--invoice li { height: 12.3px; gap: 6px; }
  .contacts--invoice svg { width: 10px; height: 10px; }
  .contacts--letter { left: 395px; top: 50px; font-size: 6px; }
  .contacts--letter li { height: 10.5px; gap: 5px; }
  .contacts--letter svg { width: 8px; height: 8px; }

  /* invoice */
  .invoice-title {
    position: absolute; left: 298px; top: 108px;
    font-family: "EB Garamond", serif;
    font-size: 38px; font-weight: 400;
    letter-spacing: 0.5px;
    color: var(--navy);
  }
  .meta-label { position: absolute; font-size: 9px; font-weight: 300; color: var(--ink-soft); }
  .rule { position: absolute; height: 1px; background: var(--ink-soft); }
  .party-head { position: absolute; font-size: 8.5px; color: var(--navy); }
  .party-lines { position: absolute; list-style: none; font-size: 8.5px; font-weight: 300; color: var(--ink-soft); line-height: 13.6px; }

  .items-head {
    position: absolute; left: 26px; top: 337px;
    width: 467px; height: 17px;
    background: var(--navy); color: #fff;
    font-size: 9px;
  }
  .items-head span { position: absolute; top: 3px; }
  .item-row {
    position: absolute; left: 26px; width: 462px; height: 19.5px;
    font-size: 9px; color: var(--navy);
  }
  .item-row--shaded { background: linear-gradient(90deg, var(--row-shade), #f4f4f5 95%, #fff); }
  .item-row span { position: absolute; top: 4.5px; }
  .item-row .cell-desc { left: 0; }
  .item-row .cell-num { font-size: 7.5px; color: var(--ink); top: 5.5px; transform: translateX(-50%); }
  .center { transform: translateX(-50%); }

  .total-bar {
    position: absolute; left: 26px; top: 490px;
    width: 467px; height: 16px;
    background: var(--navy); color: #fff;
    font-size: 7.5px; font-weight: 500;
  }
  .total-bar span { position: absolute; top: 3.5px; }

  .notes-head { position: absolute; left: 26px; top: 543px; font-size: 6px; font-weight: 500; color: var(--navy); }
  .notes-body {
    position: absolute; left: 26px; top: 553px; width: 91px;
    font-size: 5px; line-height: 7.5px; text-align: justify; color: var(--ink);
  }
  .thanks { position: absolute; left: 196px; top: 557px; font-size: 9.5px; font-style: italic; font-weight: 300; color: var(--ink-soft); }
  .sign-label { position: absolute; left: 415px; top: 615px; transform: translateX(-50%); font-size: 9px; color: var(--navy); }

  /* letter */
  .watermark {
    position: absolute; left: 175px; top: 118px;
    width: 318px; height: 318px; border-radius: 50%;
    background: var(--watermark);
  }
  .salutation {
    position: absolute; left: 139px; top: 164px;
    font-family: "EB Garamond", serif; font-size: 23px; font-weight: 400; color: var(--navy);
  }
  .letter-body { position: absolute; left: 139px; top: 212px; width: 353px; }
  .letter-body p {
    font-size: 8.9px; line-height: 14.35px; text-align: justify;
    color: var(--ink); margin-bottom: 14.4px;
  }
  .closing {
    position: absolute; right: 27px; top: 541px;
    text-align: right; list-style: none;
    font-size: 7.5px; line-height: 14.5px; color: var(--navy);
  }
</style>
</head>
<body>

<svg width="0" height="0" style="position:absolute">
  <defs>
    <symbol id="icon-phone" viewBox="0 0 10 10">
      <rect width="10" height="10" rx="1.5" fill="#16253a"/>
      <path d="M3 2.2c.4-.2.7 0 .9.4l.4.8c.1.3 0 .5-.2.7l-.3.3c.3.7.8 1.2 1.5 1.5l.3-.3c.2-.2.4-.3.7-.2l.8.4c.4.2.6.5.4.9-.3.7-.9 1.1-1.6.9C4.6 7.2 2.8 5.4 2.4 3.8c-.2-.7.1-1.3.6-1.6z" fill="#fff"/>
    </symbol>
    <symbol id="icon-fax" viewBox="0 0 10 10">
      <rect width="10" height="10" rx="1.5" fill="#16253a"/>
      <rect x="3" y="2" width="4" height="2" fill="none" stroke="#fff" stroke-width=".7"/>
      <rect x="2" y="4" width="6" height="3" rx=".5" fill="none" stroke="#fff" stroke-width=".7"/>
      <rect x="3" y="6" width="4" height="2" fill="#fff"/>
    </symbol>
    <symbol id="icon-pin" viewBox="0 0 10 10">
      <rect width="10" height="10" rx="1.5" fill="#16253a"/>
      <path d="M5 1.8a2.4 2.4 0 0 0-2.4 2.4C2.6 6 5 8.4 5 8.4S7.4 6 7.4 4.2A2.4 2.4 0 0 0 5 1.8z" fill="#fff"/>
      <circle cx="5" cy="4.2" r=".9" fill="#16253a"/>
    </symbol>
  </defs>
</svg>

<!-- Invoice sheet -->
<section class="sheet sheet--invoice" aria-label="Invoice">
  <div class="brand">
    <div class="brand__disc"></div>
    <div class="brand__name">Halden<br>Law PLC</div>
  </div>

  <ul class="contacts contacts--invoice">
    <li><svg><use href="#icon-phone"/></svg>00000 00 00</li>
    <li><svg><use href="#icon-fax"/></svg>00000 00 00</li>
    <li><svg><use href="#icon-pin"/></svg>0000 xxxxxxx-xxxxxx</li>
  </ul>

  <h1 class="invoice-title">INVOICE</h1>

  <span class="meta-label" style="left:350px;top:179px;">DATE</span>
  <div class="rule" style="left:383px;top:188px;width:109px;"></div>
  <span class="meta-label" style="left:350px;top:193px;">INVOICE NO.</span>
  <div class="rule" style="left:420px;top:202px;width:72px;"></div>

  <span class="party-head" style="left:26px;top:216px;">BILL TO</span>
  <div class="rule" style="left:26px;top:228px;width:198px;"></div>
  <ul class="party-lines" style="left:26px;top:229px;">
    <li>Contact Name</li>
    <li>Client Company Name</li>
    <li>Address</li>
    <li>Phone</li>
    <li>Email</li>
  </ul>

  <span class="party-head" style="left:259px;top:216px;">SHIP TO</span>
  <div class="rule" style="left:259px;top:228px;width:234px;"></div>
  <ul class="party-lines" style="left:259px;top:229px;">
    <li>Name / Dept</li>
    <li>Client Company Name</li>
    <li>Address</li>
    <li>Phone</li>
  </ul>

  <div class="items-head">
    <span style="left:1px;">ITEM DESCRIPTION</span>
    <span class="center" style="left:272px;">UNITE PRICE</span>
    <span class="center" style="left:350px;">QUANTITY</span>
    <span class="center" style="left:427px;">TOTAL</span>
  </div>

  <div class="item-row item-row--shaded" style="top:373px;">
    <span class="cell-desc">DESCRIPTION</span>
    <span class="cell-num" style="left:275px;">$0.00</span>
    <span class="cell-num" style="left:350px;">2</span>
    <span class="cell-num" style="left:429px;">0.00</span>
  </div>
  <div class="item-row" style="top:392.5px;">
    <span class="cell-desc">DESCRIPTION</span>
    <span class="cell-num" style="left:275px;">$0.00</span>
    <span class="cell-num" style="left:350px;">1</span>
    <span class="cell-num" style="left:429px;">0.00</span>
  </div>
  <div class="item-row item-row--shaded" style="top:412px;">
    <span class="cell-desc">DESCRIPTION</span>
    <span class="cell-num" style="left:275px;">$0.00</span>
    <span class="cell-num" style="left:350px;">1</span>
    <span class="cell-num" style="left:429px;">0.00</span>
  </div>
  <div class="item-row" style="top:431.5px;">
    <span class="cell-desc">DESCRIPTION</span>
    <span class="cell-num" style="left:275px;">$0.00</span>
    <span class="cell-num" style="left:350px;">1</span>
    <span class="cell-num" style="left:429px;">0.00</span>
  </div>
  <div class="item-row item-row--shaded" style="top:451px;">
    <span class="cell-num" style="left:275px;">$0.00</span>
    <span class="cell-num" style="left:350px;">1</span>
    <span class="cell-num" style="left:429px;">0.00</span>
  </div>

  <div class="total-bar">
    <span class="center" style="left:183px;">TOTAL TAX</span>
    <span style="right:15px;">0.00</span>
  </div>

  <span class="notes-head">NOTES:</span>
  <p class="notes-body">Lorem ipsum dolor sit amet, consectetuer adipiscing elit, sed diam nonummy nibh euismod tincidunt ut laoreet</p>

  <span class="thanks">Thank you for your business</span>

  <div class="rule" style="left:337px;top:610px;width:156px;"></div>
  <span class="sign-label">Authorized sign</span>
</section>

<!-- Letterhead sheet -->
<section class="sheet sheet--letter" aria-label="Letterhead">
  <div class="watermark" aria-hidden="true"></div>

  <div class="brand">
    <div class="brand__disc"></div>
    <div class="brand__name">Halden<br>Law PLC</div>
  </div>

  <ul class="contacts contacts--letter">
    <li><svg><use href="#icon-phone"/></svg>00000 00 00</li>
    <li><svg><use href="#icon-fax"/></svg>00000 00 00</li>
    <li><svg><use href="#icon-pin"/></svg>0000 xxxxxxx-xxxxxx</li>
  </ul>

  <h2 class="salutation">Dear Sir</h2>

  <div class="letter-body">
    <p>Lorem ipsum dolor sit amet, consectetuer adipiscing elit, sed diam nonummy nibh euismod tincidunt ut laoreet dolore magna aliquam erat volutpat. Ut wisi enim ad minim veniam, quis nostrud exerci tation ullamcorper suscipit lobortis nisl ut aliquip ex ea commodo consequat. Duis autem vel eum iriure dolor in hendrerit in vulputate velit esse molestie consequat, vel illum dolore eu feugiat nulla facilisis at vero eros et accumsan et iusto odio dignissim qui blandit praesent luptatum zzril delenit augue duis dolore te feugait nulla facilisi.</p>
    <p>Lorem ipsum dolor sit amet, cons ectetuer adipiscing elit, sed diam nonummy nibh euismod tincidunt ut laoreet dolore magna aliquam erat volutpat. Ut wisi enim ad minim veniam, quis nostrud exerci tation ullamcorper suscipit lobortis nisl ut aliquip ex ea commodo consequat.</p>
    <p>Lorem ipsum dolor sit amet, consectetuer adipiscing elit, sed diam nonummy nibh euismod tincidunt ut laoreet dolore magna aliquam erat volutpat. Ut wisi enim ad minim veniam, quis nostrud exerci tation ullamcorper suscipit lobortis nisl ut aliquip ex ea commodo consequat. Duis autem vel eum iriure dolor in hendrerit in vulputate velit esse molestie consequat, vel illum dolore eu feugiat nulla facilisis at vero eros et accumsan et iusto odio dignissim qui blandit praesent luptatum zzril delenit augue duis dolore te feugait nulla facilisi.</p>
  </div>

  <ul class="closing">
    <li>xxxxx</li>
    <li>xxxxxxxxx</li>
    <li>xxxxxxxxxxxxxxxx</li>
    <li>xxxxxxxx</li>
  </ul>

  <div class="rule" style="left:348px;top:623px;width:144px;"></div>
</section>

</body>
</html>
```